Salt, Silence and Sunrise Redesign

I am looking for a redesign on my book cover. I would like to keep the same title, subtitle and author name. This book is for women between the ages of 45 - 55 that are also dealing with health and hormone issues. So if there's a photo used of a woman, it should reflect that age group and a look of frustration or hopelessness. I would also like a notation that I am a best selling author and second edition. I have attached the current book cover and a copy of my business logo. Perhaps some consistency with my business logo would be a good idea and not necessary.
I have also attached an updated back cover with an edit in text and a new picture.
If it's helpful, I am a natural doctor known as a Traditional Naturopath and my primary focus of business is helping women overcome menopause symptoms.
Note, I do not want the use of any medical pictures, such as a stethoscope or a doctor in a white coat.
I am looking for different look and theme from my current cover. Something that is a bit more luxurious or upscale from my past cover.

```html
<!DOCTYPE html>
<html lang="en">
<head>
<meta charset="utf-8">
<title>Salt, Silence and Sunrise – Second Edition Book Cover</title>
<link href="https://fonts.googleapis.com/css2?family=Playfair+Display:wght@600;700&family=Cormorant+Garamond:ital,wght@0,500;0,600;1,500&family=Nunito+Sans:wght@400;600;700&display=swap" rel="stylesheet">
<style>
  :root {
    --stage: #efefef;
    --ink: #17161a;
    --ink-soft: #24222a;
    --ivory: #faf7f1;
    --gold: #c8a96a;
    --gold-light: #e2cc9a;
    --text-light: #eeeae2;
    --text-dark: #1d1b20;
    --photo-a: #c9c4c0;
    --photo-b: #7b7478;
    --portrait-a: #ddd6dc;
    --portrait-b: #a195a8;
  }
  * { box-sizing: border-box; margin: 0; padding: 0; }
  html, body { width: 1200px; height: 800px; overflow: hidden; }
  body {
    background: var(--stage);
    font-family: "Nunito Sans", "Helvetica Neue", Arial, sans-serif;
    position: relative;
  }
  .cover {
    position: absolute;
    top: 40px;
    width: 480px;
    height: 720px;
    overflow: hidden;
    box-shadow: 0 10px 30px rgba(0,0,0,0.2);
  }
  .cover--back {
    left: 90px;
    background: linear-gradient(var(--ink) 0 74%, var(--ivory) 74% 100%);
  }
  .cover--front {
    left: 630px;
    background: linear-gradient(180deg, var(--ink-soft) 0%, var(--ink) 64%, var(--ivory) 64% 100%);
  }
  .gold-rule {
    position: absolute;
    left: 20px; right: 20px; top: 20px; bottom: 20px;
    border: 1px solid var(--gold);
    opacity: 0.55;
    pointer-events: none;
  }

  /* Back cover */
  .back-title {
    font-family: "Playfair Display", Georgia, serif;
    font-weight: 700;
    color: var(--gold);
    font-size: 30px;
    text-align: center;
    margin-top: 46px;
    line-height: 1.15;
  }
  .back-subtitle {
    border-top: 1px solid var(--gold);
    border-bottom: 1px solid var(--gold);
    color: var(--gold-light);
    font-family: "Cormorant Garamond", Georgia, serif;
    font-style: italic;
    font-size: 19px;
    text-align: center;
    margin: 8px 48px 0;
    padding: 3px 0;
  }
  .back-body { padding: 18px 44px 0; }
  .author-portrait {
    float: left;
    width: 150px;
    height: 196px;
    margin: 3px 14px 6px 0;
    border: 2px solid var(--gold);
    background: linear-gradient(160deg, var(--portrait-a), var(--portrait-b));
  }
  .back-copy {
    color: var(--text-light);
    font-size: 14px;
    line-height: 1.45;
  }

  /* Front cover */
  .edition {
    position: absolute;
    top: 38px; left: 0; right: 0;
    text-align: center;
    font-size: 11px;
    font-weight: 700;
    letter-spacing: 4px;
    text-transform: uppercase;
    color: var(--gold);
  }
  .front-title {
    font-family: "Playfair Display", Georgia, serif;
    font-weight: 700;
    color: var(--gold);
    font-size: 52px;
    line-height: 1.08;
    text-align: center;
    margin-top: 66px;
  }
  .front-subtitle {
    font-family: "Cormorant Garamond", Georgia, serif;
    font-style: italic;
    font-weight: 500;
    color: var(--text-light);
    font-size: 26px;
    line-height: 1.25;
    text-align: center;
    margin: 14px 50px 0;
  }
  .cover-photo {
    position: absolute;
    left: 58px;
    top: 352px;
    width: 290px;
    height: 250px;
    border: 2px solid var(--gold);
    background: linear-gradient(150deg, var(--photo-a), var(--photo-b));
  }
  .bestseller-badge {
    position: absolute;
    left: 362px;
    top: 530px;
    width: 88px;
    height: 88px;
  }
  .front-credit {
    position: absolute;
    left: 0;
    right: 0;
    top: 622px;
    text-align: center;
    line-height: 1.25;
  }
  .credit-note {
    font-size: 10px;
    font-weight: 700;
    letter-spacing: 3px;
    text-transform: uppercase;
    color: var(--gold);
  }
  .author-name {
    font-family: "Playfair Display", Georgia, serif;
    font-weight: 600;
    font-size: 20px;
    color: var(--text-dark);
  }
  .author-role { font-weight: 600; font-size: 14px; color: var(--text-dark); letter-spacing: 1px; }
  .foreword {
    font-family: "Cormorant Garamond", Georgia, serif;
    font-style: italic;
    font-size: 17px;
    color: #9a7d45;
  }
</style>
</head>
<body>

  <section class="cover cover--back" aria-label="Back cover">
    <div class="gold-rule"></div>
    <h2 class="back-title">Salt, Silence and Sunrise?</h2>
    <p class="back-subtitle">How to Reserve the Clock and Feel Young Again</p>
    <div class="back-body">
      <div class="author-portrait" role="img" aria-label="Portrait photo of the author"></div>
      <p class="back-copy">Imagine how good it feels when you are able to easily slip into your sexy skinny jeans, have energy all day and feel young again. "Salt, Silence and Sunrise?" provides proven and effective secrets that give you the ability to achieve this all and get your life back on many levels. It's a book that explains the how and why you became overweight, fatigued and frustrated and outlines simple, effective, and proven steps in a way that will have you slipping on your skinny jeans, having abundant energy and returning to your youth. You can reverse the clock!</p>
    </div>
  </section>

  <section class="cover cover--front" aria-label="Front cover">
    <div class="gold-rule"></div>
    <p class="edition">Second Edition</p>
    <h1 class="front-title">Salt, Silence<br>and Sunrise?</h1>
    <p class="front-subtitle">How to Reserve the Clock and Feel Young Again</p>
    <div class="cover-photo" role="img" aria-label="Photo of a tired, frustrated woman in her late forties resting after exercise"></div>
    <svg class="bestseller-badge" viewBox="0 0 100 100" role="img" aria-label="Best seller seal">
      <circle cx="50" cy="50" r="46" fill="var(--ink)" stroke="var(--gold)" stroke-width="3"/>
      <circle cx="50" cy="50" r="37" fill="none" stroke="var(--gold)" stroke-width="1.5"/>
    </svg>
    <div class="front-credit">
      <p class="credit-note">Best-Selling Author</p>
      <p class="author-name">Marten Coleby</p>
      <p class="author-role">Traditional Naturapath</p>
      <p class="foreword">Foreword by Dr. Avery Lindqvist</p>
    </div>
  </section>

</body>
</html>
```